Flyer Design

I need a nice professional flyer design to use for advertising my lawn/snow removal business. Flyers I am using are 5.47"x4.21". I've attached a flyer I found online that I liked. Just wanting something creative and professional. The images of the logos I attached are of the original logo design, and the new color design we are using. There is also a mockup of our tshirt design to give you an idea of the actual color on the tshirt, since the jpeg logo isn't exactly accurate on color.
Things I need on the flyer in no particular order:
"Snow is coming"
"Don't Wait Until It's TOO LATE!"
"Free Estimates"
Services offered
"Commercial/Residential"
"Snow Plowing"
"Snow Blowing"
"Snow Shoveling"
"Ice Removal"
"Salting/Sanding"
"Fully Licensed and Insured"
"Available and ON CALL 24/7"
"Seasonal Packages Available"
"CALL NOW TO RESERVE"

```html
<!DOCTYPE html>
<html lang="en">
<head>
<meta charset="utf-8">
<title>Snow Removal Flyer</title>
<link href="https://fonts.googleapis.com/css2?family=Noto+Serif:wght@400;700&family=Open+Sans:wght@700&display=swap" rel="stylesheet">
<style>
  :root {
    --orange: #f26a12;
    --orange-text: #f06c14;
    --ink: #1c1c1c;
    --white: #ffffff;
    --snow-light: #f4f4f4;
    --snow-mid: #d9d9d9;
    --stripe: #6c6c6c;
    --backdrop: #e9e6e2;
  }
  * { margin: 0; padding: 0; box-sizing: border-box; }
  html, body { width: 1200px; height: 1199px; overflow: hidden; }
  body {
    background: var(--backdrop);
    font-family: "Noto Serif", Georgia, serif;
    position: relative;
  }
  .flyer {
    position: absolute;
    left: 118px; top: 228px;
    width: 964px; height: 742px;
    background: var(--ink);
    overflow: hidden;
    box-shadow: 0 6px 16px rgba(0,0,0,0.25);
  }
  .snow-photo {
    position: absolute; left: 0; top: 0; width: 964px; height: 420px;
    background: linear-gradient(100deg, #c9cbcd 0%, #eef0f1 35%, var(--snow-light) 60%, var(--snow-mid) 100%);
  }
  .panel-shape { position: absolute; left: 0; top: 0; }
  .brand {
    position: absolute; left: 520px; top: 100px; width: 390px;
    display: flex; align-items: center; justify-content: center; gap: 14px;
  }
  .brand-dot { width: 26px; height: 26px; border-radius: 50%; background: var(--orange); flex: none; }
  .brand-name {
    font-weight: 700; font-size: 34px; line-height: 1.15; color: var(--ink); text-align: left;
  }
  .headline {
    position: absolute; left: 420px; width: 544px; top: 272px; text-align: center;
  }
  .headline h1 {
    font-size: 50px; font-weight: 700; color: var(--orange-text); line-height: 1.1; letter-spacing: 0.5px;
  }
  .headline p { font-size: 26px; font-weight: 700; color: var(--ink); line-height: 1.25; margin-top: 2px; }
  .services {
    position: absolute; left: 35px; top: 293px; width: 370px; height: 415px;
    background: var(--orange); color: var(--white); padding: 30px 0 0 24px;
  }
  .services h2 { font-size: 38px; font-weight: 700; line-height: 1.1; }
  .services .market { font-size: 25px; margin-top: 6px; }
  .service-list { list-style: none; margin-top: 30px; padding-left: 18px; }
  .service-list li {
    font-size: 29px; height: 46.5px; display: flex; align-items: center; gap: 12px;
  }
  .service-list svg { width: 32px; height: 32px; flex: none; }
  .details {
    position: absolute; left: 450px; width: 500px; top: 438px; text-align: center; color: var(--white);
  }
  .details .line { font-size: 26px; line-height: 32px; }
  .details .accent { color: var(--orange-text); font-weight: 700; }
  .details .cta { font-size: 36px; font-weight: 700; color: var(--orange-text); margin-top: 28px; line-height: 1.2; }
  .details .phone {
    font-family: "Open Sans", Arial, sans-serif; font-weight: 700; font-size: 62px;
    color: var(--orange-text); line-height: 1.05; letter-spacing: -0.5px;
  }
  .details .estimates { font-size: 36px; font-weight: 700; margin-top: 6px; }
</style>
</head>
<body>
  <div class="flyer">
    <div class="snow-photo" role="img" aria-label="White pickup truck with a red snow plow pushing through a snowy road"></div>
    <svg class="panel-shape" width="964" height="742" viewBox="0 0 964 742" aria-hidden="true">
      <path d="M0 190 C 60 235, 120 270, 170 300 L 405 300 L 405 394 C 600 402, 800 412, 964 408 L 964 742 L 0 742 Z" fill="#1c1c1c"/>
      <path d="M405 378 C 600 384, 800 394, 964 388 L 964 408 C 800 412, 600 402, 405 394 Z" fill="#6c6c6c"/>
    </svg>

    <div class="brand">
      <span class="brand-dot"></span>
      <span class="brand-name">Summit Ridge Lawn<br>&amp; Landscape LLC</span>
    </div>

    <div class="headline">
      <h1>SNOW IS COMING</h1>
      <p>Don't Wait Until It's TOO LATE!</p>
    </div>

    <section class="services">
      <h2>Services Offered</h2>
      <p class="market">Commercial - Residential</p>
      <ul class="service-list">
        <li><svg viewBox="0 0 24 24"><path fill="#fff" d="M12 1.5l3.1 6.6 7.2.8-5.4 4.9 1.5 7.1L12 17.3l-6.4 3.6 1.5-7.1L1.7 8.9l7.2-.8z"/></svg>Snow Plowing</li>
        <li><svg viewBox="0 0 24 24"><path fill="#fff" d="M12 1.5l3.1 6.6 7.2.8-5.4 4.9 1.5 7.1L12 17.3l-6.4 3.6 1.5-7.1L1.7 8.9l7.2-.8z"/></svg>Snow Blowing</li>
        <li><svg viewBox="0 0 24 24"><path fill="#fff" d="M12 1.5l3.1 6.6 7.2.8-5.4 4.9 1.5 7.1L12 17.3l-6.4 3.6 1.5-7.1L1.7 8.9l7.2-.8z"/></svg>Snow Shoveling</li>
        <li><svg viewBox="0 0 24 24"><path fill="#fff" d="M12 1.5l3.1 6.6 7.2.8-5.4 4.9 1.5 7.1L12 17.3l-6.4 3.6 1.5-7.1L1.7 8.9l7.2-.8z"/></svg>Ice Removal</li>
        <li><svg viewBox="0 0 24 24"><path fill="#fff" d="M12 1.5l3.1 6.6 7.2.8-5.4 4.9 1.5 7.1L12 17.3l-6.4 3.6 1.5-7.1L1.7 8.9l7.2-.8z"/></svg>Salting/Sanding</li>
      </ul>
    </section>

    <section class="details">
      <p class="line">Fully Licensed and Insured</p>
      <p class="line accent">AVAILABLE AND ON CALL 24/7</p>
      <p class="line">Seasonal Packages Available</p>
      <p class="cta">Call Now to Reserve</p>
      <p class="phone">123-456-7890</p>
      <p class="estimates">Free Estimates</p>
    </section>
  </div>
</body>
</html>
```